Brisk Bookings needs a New Home page

We provide online appointment scheduling. There are many schedulers out there. Ours is unique because the scheduler is shown in one compact view that can be easily incorporated into the customer's website or Chatterbay page. Whether our customer is a solo hair-stylist or a large testing center with hundreds of testing seats at multiple locations, our customer still gets the same easy-to-use, one-page scheduling experience.

Our current home page, briskbookings.example, feels cluttered and outdated. We want something more modern and minimal.

Here are web pages we like:
artmosaic.example
tillquay.example
ruvel.example

We are not unhappy with the current logo or color scheme.

Need very clear call(s) to action (i.e. sign up for trial, schedule a demo).
Design needs to look good on devices of varying size.

Here are some ideas:
“Simple Online Scheduling” - Simple, compact design, easy-to-use & powerful, time-saving, chaos-taming, affordable, one page scheduling
“Stay in touch” - Basic email confirmations, reminders or targeted email notifications for follow-ups, no shows and more
“Multiple locations? No problem” - Schedule for multiple locations on one scheduler -
“Resource Pools” - Batting cages, clerks at the DMV, computers in a lab, pilates reformer machines
“Go Social” - Scheduling for Chatterbay and mobile devices
“Visual Reporting” - Reports
“Trusted” - Testimonials, reliable since 2005, etc.
List of industries (with links to industry-specific pages)

Ultimately want to redevelop the full site.
Updates

Reason: Please do not submit any new designs. We are now just wrapping up polling and discussing details. Thank you to all designers who have submitted. We feel lucky to get to chose from many great designs.

Target Market(s)

Audience is very broad including solo entrepreneurs (massage therapist, accountants, lawyers), educational institutions (elementary schools, university departments, advisers, testing centers), health care providers and screening services, to government.

Industry/Entity Type

Online

Requirements
Must have
• Call(s) to action, i.e. sign up for trial, schedule a demo.
• Look good on devices of different sizes.

```html
<!DOCTYPE html>
<html lang="en">
<head>
<meta charset="utf-8">
<title>Brisk Bookings – Simple Online Scheduling</title>
<link rel="stylesheet" href="https://fonts.googleapis.com/css2?family=Lato:wght@300;400&display=swap">
<style>
  :root{
    --paper:#efefef;
    --ink:#2b2b2b;
    --muted:#a9a9a9;
    --green:#9cc300;
    --green-text:#8fb800;
    --dark-tab:#4a4a4a;
    --white:#ffffff;
    --emboss-light:#f7f7f7;
    --emboss-mid:#dcdcdc;
  }
  *{box-sizing:border-box;margin:0;padding:0}
  html,body{width:1200px;height:900px;overflow:hidden}
  body{
    position:relative;
    background:var(--paper);
    font-family:"Lato",sans-serif;
    font-weight:300;
    color:var(--ink);
  }
  .brand{
    position:absolute;left:22px;top:22px;
    display:flex;align-items:center;gap:8px;
    font-size:24px;font-weight:300;color:#6d6d6d;letter-spacing:-0.3px;
  }
  .brand-dot{width:10px;height:10px;border-radius:50%;background:var(--green)}
  .top-tabs{position:absolute;top:0;right:7px;display:flex;gap:7px}
  .top-tabs a{
    display:block;width:100px;height:33px;padding-top:16px;
    background:var(--dark-tab);color:var(--white);
    font-size:12px;font-weight:400;text-align:center;text-decoration:none;
  }
  .hero-title{
    position:absolute;left:295px;top:187px;
    font-size:30px;line-height:36px;font-weight:300;letter-spacing:0.4px;
  }
  .cta{
    position:absolute;left:293px;top:324px;width:152px;height:44px;
    background:var(--green);color:var(--ink);
    font-size:15px;font-weight:300;line-height:44px;text-align:center;text-decoration:none;
  }
  .slide-arrow{
    position:absolute;top:251px;width:60px;height:60px;border-radius:50%;
    background:var(--white);
  }
  .slide-arrow svg{width:60px;height:60px;display:block}
  .slide-prev{left:159px}
  .slide-next{left:926px}
  .calendar-art{
    position:absolute;left:535px;top:155px;width:325px;height:270px;
    border-radius:40% 45% 30% 35%;
    background:radial-gradient(ellipse at 45% 50%, var(--emboss-mid) 0%, #e6e6e6 45%, var(--paper) 75%);
  }
  .scroll-cue{position:absolute;left:349px;top:462px}
  .main-nav{
    position:absolute;left:0;top:516px;width:1200px;height:88px;background:var(--green);
  }
  .nav-notch{position:absolute;left:317px;top:0}
  .main-nav ul{
    list-style:none;display:flex;gap:6px;
    position:absolute;left:303px;top:32px;font-size:15px;
  }
  .main-nav li{color:var(--ink)}
  .main-nav li.current{color:var(--white)}
  .product-shot{
    position:absolute;left:283px;top:659px;width:377px;height:139px;
    background:linear-gradient(135deg,#d9dbc4 0%,#a3a78a 45%,#6f7260 100%);
  }
  .section-title{font-size:29px;font-weight:300;letter-spacing:0.5px}
  .intro{position:absolute;left:705px;top:652px;width:370px}
  .intro p{
    margin-top:16px;font-size:13.5px;line-height:17px;
    text-transform:uppercase;color:var(--muted);white-space:nowrap;
  }
  .intro em{font-style:normal;color:var(--green-text)}
  .more{display:block;margin-top:14px;margin-left:3px;font-size:22px;color:var(--ink);text-decoration:none}
  .features-title{position:absolute;left:282px;top:876px}
</style>
</head>
<body>
  <header>
    <div class="brand"><span>briskbookings</span><span class="brand-dot"></span></div>
    <nav class="top-tabs">
      <a href="#">ACCOUNT LOGIN</a>
      <a href="#">CONTACT US</a>
    </nav>
  </header>

  <section class="hero">
    <h1 class="hero-title">SIMPLE<br>ONLINE<br>SCHEDULING</h1>
    <a class="cta" href="#">GET STARTED</a>

    <a class="slide-arrow slide-prev" href="#" aria-label="Previous slide">
      <svg viewBox="0 0 60 60"><path d="M34 18 L22 30 L34 42 M42 18 L30 30 L42 42" fill="none" stroke="#cfcfcf" stroke-width="5"/></svg>
    </a>
    <a class="slide-arrow slide-next" href="#" aria-label="Next slide">
      <svg viewBox="0 0 60 60"><path d="M26 18 L38 30 L26 42 M18 18 L30 30 L18 42" fill="none" stroke="#cfcfcf" stroke-width="5"/></svg>
    </a>

    <div class="calendar-art" role="img" aria-label="Embossed month calendar illustration with day 17 highlighted in green"></div>

    <svg class="scroll-cue" width="20" height="24" viewBox="0 0 20 24" aria-label="Scroll down">
      <path d="M2 4 L10 20 L18 4" fill="none" stroke="#666" stroke-width="1.3"/>
    </svg>
  </section>

  <nav class="main-nav">
    <svg class="nav-notch" width="20" height="19" viewBox="0 0 20 19"><path d="M0 0 H20 L10 19 Z" fill="var(--white)"/></svg>
    <ul>
      <li class="current">HOME</li>
      <li>SEE IT WORK</li>
      <li>WHO IT´S FOR</li>
      <li>OUR SCHEDULER</li>
      <li>FREE TRIAL</li>
      <li>DIG IN</li>
      <li>ABOUT US</li>
    </ul>
  </nav>

  <main>
    <div class="product-shot" role="img" aria-label="Laptop showing the scheduler's one-page booking view"></div>
    <section class="intro">
      <h2 class="section-title">ONLINE SCHEDULER</h2>
      <p>Brisk Bookings wants to help you <em>save</em><br><em>time, increase customer appointments</em> and be a<br>better partner to your clients. Our appoint-<br>ment scheduler is <em>used by thousands</em> world-<br>wide because we strive to be the company you<br>want to do business with.</p>
      <a class="more" href="#">&gt;</a>
    </section>
    <h2 class="section-title features-title">GENERAL FEATURES:</h2>
  </main>
</body>
</html>
```